依頼詳細
運動の嫌いな子でも気軽に身体を動かせるような教室を目指しています。
現在は低学年の女子が主な受講生なので、男子や高学年の子ども達にも興味を持っていただけたらありがたいです。
配布方法は新聞への折り込みなどを考えています。
白黒で印刷してもキレイに見えるデザインを希望します。
記載項目
現在使っているチラシ(wordファイル)を添付しています。
記載項目はその内容でお願いいたします。
サイズ
A4
ページ数
片面
希望イメージ
シンプル 複雑
単色 カラフル
暗い 明るい
日常 高級
遊び心 厳粛
未来的 伝統的
女性的 男性的
希望する色
納品ファイル
• 高解像度JPG (.jpg)
補足説明
■ 選んだ理由

ぱっと目を引く明るいデザインと、雰囲気が当教室とマッチしていることから決定いたしました。
PRポインとや、目線の流れもわかりやすく、白黒バージョンも見やすかったです。

■ 提案者全員のお礼・コメント

ご提案いただいた皆様
この度は沢山のご提案をいただき、まことにありがとうございました。
初めてのポルテミカの利用でしたが、素晴らしいご提案をたくさんいただけたことに感激しました。
ぜひこれからも依頼させていただきたいと思います。
よろしくお願いいたします。

```html
<!DOCTYPE html>
<html lang="ja">
<head>
<meta charset="utf-8">
<title>みなもとキッズダンス 川辺教室のご案内</title>
<link href="https://fonts.googleapis.com/css2?family=M+PLUS+Rounded+1c:wght@400;700;800;900&display=swap" rel="stylesheet">
<style>
  :root{
    --cream:#fdf1d2;
    --dot:#f8e2ad;
    --pink:#e6357a;
    --pink-soft:#f7c6d8;
    --purple:#3a2b86;
    --orange:#f08a00;
    --blue:#7fb3e2;
    --ink:#222;
    --red:#d8262f;
    --gray:#e9e9e9;
    --white:#fff;
    --yellow:#ffe04a;
  }
  *{box-sizing:border-box;margin:0;padding:0}
  html,body{width:849px;height:1200px;overflow:hidden}
  body{font-family:"M PLUS Rounded 1c",sans-serif;color:var(--ink);background:var(--white)}
  .flyer{position:relative;width:849px;height:1200px;overflow:hidden;
    background:var(--cream);
    background-image:radial-gradient(var(--dot) 3px,transparent 3.5px);
    background-size:22px 22px;}
  .abs{position:absolute}
  .title-card{left:118px;top:14px;width:613px;height:132px;background:var(--white);
    border-radius:22px;border:4px solid var(--pink);text-align:center;padding-top:10px}
  .title-card h1{font-weight:900;color:var(--pink);font-size:46px;line-height:56px;letter-spacing:2px;white-space:nowrap}
  .title-card h1 span{display:block;color:var(--purple)}
  .kid{top:150px;width:230px;height:228px;border-radius:50% 50% 40% 40%;
    background:linear-gradient(180deg,#ffd9a8,#f6b24d 55%,#7cc4e8)}
  .kid.left{left:22px}
  .kid.right{left:598px;background:linear-gradient(180deg,#ffd9a8,#f59ac0 55%,#a98fd8)}
  .day{left:282px;top:158px;width:285px;height:48px;background:var(--pink);color:var(--white);
    font-weight:900;font-size:36px;text-align:center;line-height:48px;border-radius:8px;letter-spacing:4px;white-space:nowrap}
  .time{left:232px;top:208px;width:385px;text-align:center;font-weight:900;font-size:36px;letter-spacing:1px;white-space:nowrap}
  .place{left:222px;top:254px;width:405px;text-align:center;font-size:16px;font-weight:700;white-space:nowrap}
  .fee{left:244px;top:282px;width:362px;height:52px;background:var(--white);border:3px solid var(--ink);
    border-radius:10px;text-align:center;font-weight:900;font-size:30px;line-height:46px;white-space:nowrap}
  .fee small{font-size:18px}
  .fee-note{left:214px;top:340px;width:421px;text-align:center;font-size:12px;color:var(--red);font-weight:700;line-height:18px;white-space:nowrap}
  .band{left:0;top:380px;width:849px;height:186px;background:var(--purple);color:var(--white)}
  .request{left:16px;top:394px;width:100px;height:100px;border-radius:50%;background:var(--orange);
    color:var(--white);font-weight:900;font-size:18px;text-align:center;display:flex;align-items:center;justify-content:center;line-height:24px}
  .songs{left:130px;top:392px;width:368px;font-size:15px;font-weight:700;line-height:25px;color:var(--white)}
  .songs strong{color:var(--yellow);font-weight:900}
  .lesson-photo{left:512px;top:396px;width:310px;height:150px;background:linear-gradient(135deg,#5f5a8f,#c9c3dd)}
  .info{left:0;top:566px;width:849px;height:410px;background:var(--white)}
  .tag{left:18px;top:596px;background:var(--orange);color:var(--white);font-weight:800;font-size:20px;padding:4px 18px;border-radius:6px}
  .teacher-photo{left:28px;top:645px;width:240px;height:200px;border-radius:12px;background:linear-gradient(180deg,#e9e4dc,#d4453c 70%,#b43630)}
  .teacher-name{left:28px;top:856px;width:240px;text-align:center;font-size:22px;font-weight:800}
  .teacher-bio{left:28px;top:890px;width:250px;font-size:13px;line-height:19px}
  .spec{left:312px;width:508px}
  .spec .label{background:var(--blue);color:var(--ink);font-weight:800;font-size:20px;text-align:center;height:32px;line-height:32px;border-radius:16px}
  .spec .value{text-align:center;font-weight:900;font-size:34px;margin-top:8px;white-space:nowrap}
  .spec .note{text-align:center;font-size:12px;line-height:17px;margin-top:2px}
  .parents{left:0;top:976px;width:849px;height:136px;background:var(--pink-soft)}
  .parents-badge{left:24px;top:990px;width:104px;height:104px;border-radius:50%;background:var(--pink);color:var(--white);
    font-weight:900;font-size:20px;display:flex;align-items:center;justify-content:center;text-align:center;line-height:26px}
  .parents ul{position:absolute;left:150px;top:18px;width:680px;list-style:none;font-size:15px;line-height:26px;font-weight:700}
  .parents li::before{content:"■";color:var(--pink);margin-right:6px}
  .contact{left:0;top:1112px;width:849px;height:88px;background:var(--gray);padding:12px 24px}
  .contact .head{font-size:16px;font-weight:800}
  .contact .tels{display:flex;gap:40px;align-items:center;margin-top:6px}
  .contact .tel{display:flex;align-items:center;gap:10px;font-size:18px;font-weight:700;white-space:nowrap}
  .contact .tel b{font-size:30px;font-weight:900;letter-spacing:1px}
</style>
</head>
<body>
<div class="flyer">
  <div class="abs title-card"><h1>みなもとキッズダンス<span>川辺教室のご案内</span></h1></div>
  <div class="abs kid left" role="img" aria-label="踊る男の子のイラスト"></div>
  <div class="abs kid right" role="img" aria-label="踊る女の子のイラスト"></div>

  <div class="abs day">毎週 水曜日</div>
  <div class="abs time">17:00～18:00</div>
  <div class="abs place">場所：川辺町ひだまりセンター 2階・研修室</div>
  <div class="abs fee">レッスン料：500円<small>/1回</small></div>
  <div class="abs fee-note">入会手続きなど必要ありません。月に1回でも、お気軽に。<br>見学は1回だけ無料です。まずはお試しください。</div>

  <div class="abs band"></div>
  <div class="abs request">リクエスト<br>歓迎!!</div>
  <p class="abs songs"><strong>アニメソング、ゲーム音楽、人気アイドル、J-POP</strong> その他ダンスミュージック<br>楽しく踊りながら、体力の向上とリズム感・調整力を養います。体力に自信のないお子様でも、気軽に参加できる教室を目指しています。</p>
  <div class="abs lesson-photo" role="img" aria-label="レッスン中の子どもたちの写真"></div>

  <div class="abs info"></div>
  <div class="abs tag">講師紹介</div>
  <div class="abs teacher-photo" role="img" aria-label="講師の写真"></div>
  <div class="abs teacher-name">森山 彩花</div>
  <p class="abs teacher-bio">山里町在住(ひかりの丘)<br>元エアロビクスインストラクター<br>ロッククライマー／カレッジ職人</p>

  <div class="abs spec" style="top:596px">
    <div class="label">対 象</div>
    <div class="value">保育園年長組～小学生</div>
    <div class="note">(保育園児は保護者の同伴をお願いしています。)<br>保護者の方もレッスン参加は無料です。</div>
  </div>
  <div class="abs spec" style="top:738px">
    <div class="label">服 装</div>
    <div class="value">動きやすい服・靴</div>
    <div class="note">※室内履きで、レッスン後の体調確認で行います。</div>
  </div>
  <div class="abs spec" style="top:856px">
    <div class="label">持ち物</div>
    <div class="value">飲み物・タオル</div>
  </div>

  <div class="abs parents">
    <ul>
      <li>教室としては、スポーツ保険に加入していません。<br>　各自スポーツ保険などへの加入をおすすめします。</li>
      <li>レッスンや発表会の写真撮影について、SNSなどへの投稿では<br>　子ども達のプライバシーにご配慮下さい。</li>
    </ul>
  </div>
  <div class="abs parents-badge">保護者<br>の方へ</div>

  <div class="abs contact">
    <div class="head">問い合わせ</div>
    <div class="tels">
      <div class="tel">川村健一 <b>080-0000-1234</b></div>
      <div class="tel">川村由紀 <b>080-0000-5678</b></div>
    </div>
  </div>
</div>
</body>
</html>
```